Rebranded Food Company looking for a new Food Label design for our packaging

We have a new logo, now we are looking for a base label for our products.
This has to comply with Australian food standards legislation - Please looks at attached brief for clarity.
We have open minds and are willing to look outside of the norm so long as it is cost effective.
It can be a label or a sleeve or a totally new concept.

Target Market(s)

85% - B2b & 15% B2C

Industry/Entity Type

Food

Font styles to use
Other font styles liked:
• Adelle / Museo

Colors

Designer to choose colors to be used in the design.

Requirements
Must have
• All the legal labelling requirements - set out in brief document
Nice to have
• Key is to see the food and not cover it all up

```html
<!DOCTYPE html>
<html lang="en">
<head>
<meta charset="utf-8">
<title>Ferncrest – Product Label System</title>
<link href="https://fonts.googleapis.com/css2?family=Zilla+Slab:wght@700&family=Roboto:wght@400;700&family=Roboto+Condensed:wght@400;700&display=swap" rel="stylesheet">
<style>
  :root {
    --lasagne: #f26b2d;
    --napoli: #ee2a4b;
    --bake: #7f411e;
    --white: #ffffff;
    --ink: #3f3f3f;
    --brand-dot: #ee2a4b;
    --wheat: #8b7a5a;
    --milk: #7fb0e0;
    --celery: #8dc63f;
    --soy: #3aa047;
    --eggs: #f7c500;
    --sulphites: #f7931e;
  }
  * { box-sizing: border-box; margin: 0; padding: 0; }
  html, body { width: 847px; height: 1200px; overflow: hidden; background: var(--white); }
  .sheet { position: relative; width: 847px; height: 1200px; }

  .label { position: absolute; width: 220px; height: 328px; border-radius: 110px; }
  .label--front { left: 56px; background: var(--c); color: var(--white); }
  .label--back { left: 305px; background: var(--white); border: 13px solid var(--c); }
  .row-1 { top: 56px; --c: var(--lasagne); }
  .row-2 { top: 421px; --c: var(--napoli); }
  .row-3 { top: 786px; --c: var(--bake); }

  /* brand name */
  .brand { display: flex; align-items: center; justify-content: center; gap: 4px;
    font-family: "Roboto", sans-serif; font-weight: 700; letter-spacing: 0.5px; }
  .brand__dot { border-radius: 50%; flex: none; }
  .label--front .brand { font-size: 19px; color: var(--white); }
  .label--front .brand__dot { width: 14px; height: 14px; background: var(--white); }
  .label--back .brand { font-size: 14px; color: var(--ink); }
  .label--back .brand__dot { width: 10px; height: 10px; background: var(--brand-dot); }

  /* front */
  .front__head { position: absolute; left: 0; right: 0; top: 0; height: 162px;
    display: flex; flex-direction: column; justify-content: flex-end; align-items: center; padding-bottom: 6px; }
  .front__title { font-family: "Zilla Slab", serif; font-weight: 700; font-size: 34px;
    line-height: 40px; text-align: center; margin-top: 6px; }
  .row-1 .front__title { margin-top: 10px; }
  .weight-ring { position: absolute; left: 55px; top: 163px; width: 110px; height: 110px;
    border-radius: 50%; background: var(--white); display: flex; align-items: center; justify-content: center; }
  .weight-ring__core { width: 66px; height: 66px; border-radius: 50%; background: var(--c);
    display: flex; align-items: center; justify-content: center;
    font-family: "Roboto", sans-serif; font-size: 13px; color: var(--white); }

  /* back */
  .back__brand { position: absolute; top: 40px; left: 0; right: 0; }
  .back__title { position: absolute; top: 64px; left: -6px; right: -6px; text-align: center;
    font-family: "Zilla Slab", serif; font-weight: 700; font-size: 22px; color: var(--c); white-space: nowrap; }
  .nutrition { position: absolute; left: 14px; top: 99px; width: 114px; height: 93px;
    border: 0.7px solid var(--ink); font-family: "Roboto Condensed", sans-serif; font-size: 3.4px; color: var(--ink); padding: 2px 3px; }
  .nutrition__head { text-align: center; font-weight: 700; line-height: 5.6px; border-bottom: 0.5px solid var(--ink); padding-bottom: 1px; }
  .nutrition table { width: 100%; border-collapse: collapse; margin-top: 1px; }
  .nutrition th, .nutrition td { text-align: right; line-height: 5.4px; font-weight: 400; }
  .nutrition th { font-weight: 700; }
  .nutrition td:first-child, .nutrition th:first-child { text-align: left; }
  .nutrition__note { position: absolute; left: 14px; top: 195px; width: 114px;
    font-family: "Roboto Condensed", sans-serif; font-size: 3.2px; color: var(--ink); }
  .ingredients { position: absolute; left: 143px; top: 99px; height: 93px; width: 24px;
    writing-mode: vertical-rl; transform: rotate(180deg);
    font-family: "Roboto Condensed", sans-serif; font-size: 3.8px; line-height: 5px; color: var(--ink); }
  .contains { position: absolute; top: 214px; left: 0; right: 0; text-align: center;
    font-family: "Zilla Slab", serif; font-weight: 700; font-size: 7.5px; color: var(--ink); letter-spacing: 0.3px; }
  .allergens { position: absolute; top: 225px; left: 22px; right: 22px; display: flex; justify-content: space-between; list-style: none; }
  .allergen { display: flex; flex-direction: column; align-items: center; gap: 1.5px;
    font-family: "Roboto Condensed", sans-serif; font-size: 2.8px; color: var(--ink); width: 18px; }
  .allergen__icon { width: 17px; height: 17px; border-radius: 50%; }
  .allergen--wheat .allergen__icon { background: var(--wheat); }
  .allergen--milk .allergen__icon { background: var(--milk); }
  .allergen--celery .allergen__icon { background: var(--celery); }
  .allergen--soy .allergen__icon { background: var(--soy); }
  .allergen--eggs .allergen__icon { background: var(--eggs); }
  .allergen--sulphites .allergen__icon { background: var(--sulphites); }
</style>
</head>
<body>
<main class="sheet">

  <!-- LASAGNE -->
  <section class="label label--front row-1">
    <div class="front__head">
      <div class="brand"><span class="brand__dot"></span>FERNCREST</div>
      <h1 class="front__title">LASAGNE</h1>
    </div>
    <div class="weight-ring"><span class="weight-ring__core">1.5kG</span></div>
  </section>
  <section class="label label--back row-1">
    <div class="brand back__brand"><span class="brand__dot"></span>FERNCREST</div>
    <h2 class="back__title">LASAGNE</h2>
    <div class="nutrition">
      <div class="nutrition__head">NUTRITION INFORMATION TYPICAL VALUES<br>SERVINGS PER PACKAGE: 0<br>SERVING SIZE: 100g</div>
      <table>
        <tr><th></th><th>Per serving</th><th>Per 100g</th></tr>
        <tr><td>Energy</td><td>1263kJ</td><td>1263kJ</td></tr>
        <tr><td></td><td>302Cal</td><td>302Cal</td></tr>
        <tr><td>Protein</td><td>13g</td><td>13g</td></tr>
        <tr><td>Fat, total</td><td>14.8g</td><td>14.8g</td></tr>
        <tr><td>– saturated</td><td>6.3g</td><td>6.3g</td></tr>
        <tr><td>Carbohydrate</td><td>28.5g</td><td>28.5g</td></tr>
        <tr><td>– sugars</td><td>4.9g</td><td>4.9g</td></tr>
        <tr><td>Sodium</td><td>756mg</td><td>756mg</td></tr>
      </table>
    </div>
    <p class="nutrition__note">All values are considered averages unless otherwise indicated</p>
    <p class="ingredients">Ingredients: wheat flour, eggs, milk, tomato, beef, celery, soy, salt, herbs, sulphites.</p>
    <p class="contains">CONTAINS</p>
    <ul class="allergens">
      <li class="allergen allergen--wheat"><span class="allergen__icon"></span>WHEAT</li>
      <li class="allergen allergen--milk"><span class="allergen__icon"></span>MILK</li>
      <li class="allergen allergen--celery"><span class="allergen__icon"></span>CELERY</li>
      <li class="allergen allergen--soy"><span class="allergen__icon"></span>SOY</li>
      <li class="allergen allergen--eggs"><span class="allergen__icon"></span>EGGS</li>
      <li class="allergen allergen--sulphites"><span class="allergen__icon"></span>SULPHITES</li>
    </ul>
  </section>

  <!-- NAPOLI SAUCE -->
  <section class="label label--front row-2">
    <div class="front__head">
      <div class="brand"><span class="brand__dot"></span>FERNCREST</div>
      <h1 class="front__title">NAPOLI<br>SAUCE</h1>
    </div>
    <div class="weight-ring"><span class="weight-ring__core">500G</span></div>
  </section>
  <section class="label label--back row-2">
    <div class="brand back__brand"><span class="brand__dot"></span>FERNCREST</div>
    <h2 class="back__title">NAPOLI SAUCE</h2>
    <div class="nutrition">
      <div class="nutrition__head">NUTRITION INFORMATION TYPICAL VALUES<br>SERVINGS PER PACKAGE: 0<br>SERVING SIZE: 100g</div>
      <table>
        <tr><th></th><th>Per serving</th><th>Per 100g</th></tr>
        <tr><td>Energy</td><td>1263kJ</td><td>1263kJ</td></tr>
        <tr><td></td><td>302Cal</td><td>302Cal</td></tr>
        <tr><td>Protein</td><td>13g</td><td>13g</td></tr>
        <tr><td>Fat, total</td><td>14.8g</td><td>14.8g</td></tr>
        <tr><td>– saturated</td><td>6.3g</td><td>6.3g</td></tr>
        <tr><td>Carbohydrate</td><td>28.5g</td><td>28.5g</td></tr>
        <tr><td>– sugars</td><td>4.9g</td><td>4.9g</td></tr>
        <tr><td>Sodium</td><td>756mg</td><td>756mg</td></tr>
      </table>
    </div>
    <p class="nutrition__note">All values are considered averages unless otherwise indicated</p>
    <p class="ingredients">Ingredients: wheat flour, eggs, milk, tomato, beef, celery, soy, salt, herbs, sulphites.</p>
    <p class="contains">CONTAINS</p>
    <ul class="allergens">
      <li class="allergen allergen--wheat"><span class="allergen__icon"></span>WHEAT</li>
      <li class="allergen allergen--milk"><span class="allergen__icon"></span>MILK</li>
      <li class="allergen allergen--celery"><span class="allergen__icon"></span>CELERY</li>
      <li class="allergen allergen--soy"><span class="allergen__icon"></span>SOY</li>
      <li class="allergen allergen--eggs"><span class="allergen__icon"></span>EGGS</li>
      <li class="allergen allergen--sulphites"><span class="allergen__icon"></span>SULPHITES</li>
    </ul>
  </section>

  <!-- BAKE IN A BOX -->
  <section class="label label--front row-3">
    <div class="front__head">
      <div class="brand"><span class="brand__dot"></span>FERNCREST</div>
      <h1 class="front__title">BAKE<br>IN A BOX</h1>
    </div>
    <div class="weight-ring"><span class="weight-ring__core">500G</span></div>
  </section>
  <section class="label label--back row-3">
    <div class="brand back__brand"><span class="brand__dot"></span>FERNCREST</div>
    <h2 class="back__title">BAKE IN A BOX</h2>
    <div class="nutrition">
      <div class="nutrition__head">NUTRITION INFORMATION TYPICAL VALUES<br>SERVINGS PER PACKAGE: 0<br>SERVING SIZE: 100g</div>
      <table>
        <tr><th></th><th>Per serving</th><th>Per 100g</th></tr>
        <tr><td>Energy</td><td>1263kJ</td><td>1263kJ</td></tr>
        <tr><td></td><td>302Cal</td><td>302Cal</td></tr>
        <tr><td>Protein</td><td>13g</td><td>13g</td></tr>
        <tr><td>Fat, total</td><td>14.8g</td><td>14.8g</td></tr>
        <tr><td>– saturated</td><td>6.3g</td><td>6.3g</td></tr>
        <tr><td>Carbohydrate</td><td>28.5g</td><td>28.5g</td></tr>
        <tr><td>– sugars</td><td>4.9g</td><td>4.9g</td></tr>
        <tr><td>Sodium</td><td>756mg</td><td>756mg</td></tr>
      </table>
    </div>
    <p class="nutrition__note">All values are considered averages unless otherwise indicated</p>
    <p class="ingredients">Ingredients: wheat flour, eggs, milk, tomato, beef, celery, soy, salt, herbs, sulphites.</p>
    <p class="contains">CONTAINS</p>
    <ul class="allergens">
      <li class="allergen allergen--wheat"><span class="allergen__icon"></span>WHEAT</li>
      <li class="allergen allergen--milk"><span class="allergen__icon"></span>MILK</li>
      <li class="allergen allergen--celery"><span class="allergen__icon"></span>CELERY</li>
      <li class="allergen allergen--soy"><span class="allergen__icon"></span>SOY</li>
      <li class="allergen allergen--eggs"><span class="allergen__icon"></span>EGGS</li>
      <li class="allergen allergen--sulphites"><span class="allergen__icon"></span>SULPHITES</li>
    </ul>
  </section>

</main>
</body>
</html>
```